Ferlande Glues

Website for funeral directors see the original website: http://pates-ferlande.be
Target Market(s)
B2C
Coding
Coded - Design and coding required
Number of Pages Required
5+ page
Font styles to use
Serif
Sans Serif
Script
Colors
9d9d9d
757575
e667a6
eea4c8
e34197
Requirements
Must have
- Keep the architecture of the current site.
Nice to have
- A page with a list of people who have died. See example: https://www.maisonbrevant.be

```html
<!DOCTYPE html>
<html lang="en">
<head>
<meta charset="utf-8">
<title>Funérailles Pâtes-Ferlande</title>
<link href="https://fonts.googleapis.com/css2?family=Poppins:wght@400;500&family=Open+Sans:wght@400;600&display=swap" rel="stylesheet">
<style>
:root{
  --pink:#d9268a;
  --pink-dark:#b71d74;
  --dark:#3a3536;
  --footer:#2f2f2f;
  --grey:#8f8f8f;
  --panel:#5f5f5f;
  --light:#e6e6e6;
  --text:#444;
  --white:#fff;
}
*{box-sizing:border-box;margin:0;padding:0}
html,body{width:1200px;height:3314px;overflow:hidden;background:var(--white)}
body{font-family:"Open Sans",sans-serif;color:var(--text);position:relative}
.wrap{position:absolute;left:144px;width:912px}
h2{font-family:"Poppins",sans-serif;font-weight:400;font-size:34px;text-align:center}
.btn{display:inline-block;font-family:"Poppins",sans-serif;font-size:12px;color:var(--pink);border:1px solid var(--pink);border-radius:16px;padding:6px 14px;text-transform:uppercase;background:var(--white)}
section{position:absolute;left:0;width:1200px}

.topbar{top:0;height:80px;background:var(--dark)}
.brand{position:absolute;left:144px;top:20px;display:flex;align-items:center;gap:14px;color:var(--white);font-family:"Poppins",sans-serif;font-size:17px}
.brand .mark{width:38px;height:38px;border-radius:50%;background:var(--white)}
.topbar .phone{position:absolute;right:144px;top:30px;color:var(--white);font-family:"Poppins",sans-serif;font-size:15px;display:flex;gap:8px;align-items:center}
.nav{top:80px;height:40px;background:var(--pink)}
.nav ul{list-style:none;display:flex;position:absolute;left:144px;height:40px}
.nav li{font-family:"Poppins",sans-serif;font-size:12.5px;color:var(--white);line-height:40px;padding:0 24px;margin-right:10px}
.nav li.active{background:var(--pink-dark)}

.hero{top:120px;height:494px;background:linear-gradient(180deg,#8a8378 0%,#6d675f 30%,#1d1d22 62%,#3a3a3c 100%)}
.hero .caption{position:absolute;bottom:18px;width:100%;text-align:center;color:var(--white);font-family:"Poppins",sans-serif;font-size:21px}
.hero .arrow{position:absolute;top:235px;width:28px;height:26px;background:#222;display:flex;align-items:center;justify-content:center}

.about{top:614px;height:312px;text-align:center}
.about h2{color:var(--pink);margin-top:70px}
.about p{font-size:11px;line-height:22.5px;margin-top:10px}
.about .btn{margin-top:14px}

.services{top:926px;height:591px;background:var(--grey)}
.services h2{color:var(--white);margin-top:70px}
.cards{position:absolute;top:127px;left:144px;display:flex;gap:10px}
.card{width:297px;height:383px;background:var(--white);text-align:center;position:relative}
.card .photo{height:190px;border-bottom:3px solid var(--pink)}
.card .icon{position:absolute;left:108px;top:150px;width:80px;height:80px;border-radius:50%;background:var(--pink);display:flex;align-items:center;justify-content:center}
.card h3{font-family:"Poppins",sans-serif;font-weight:400;font-size:16px;color:#222;margin-top:50px}
.card p{font-size:10px;line-height:15.5px;padding:6px 20px 0}
.card .btn{margin-top:12px}
.chev{position:absolute}

.steps{top:1517px;height:536px}
.steps h2{color:var(--pink);margin-top:72px}
.acc{position:absolute;left:144px;width:912px;font-family:"Poppins",sans-serif;font-size:16px;color:var(--white);padding:0 16px;display:flex;justify-content:space-between;align-items:center;height:48px}
.acc.open{background:var(--pink);height:46px}
.acc.closed{background:var(--panel)}
.acc-body{position:absolute;left:144px;width:912px;top:175px;height:112px;background:var(--light);padding:14px 16px;font-size:12px;line-height:19px}
.acc-body .btn{margin-top:8px}

.banner{top:2053px;height:399px;background:radial-gradient(ellipse at center,#4a4640 0%,#2a2a2c 60%,#1b1b1d 100%);text-align:center;color:var(--white)}
.banner p{font-family:"Poppins",sans-serif;font-size:24px;line-height:37px;margin-top:140px}
.banner .btn{background:transparent;color:var(--white);border-color:var(--white);margin-top:4px}

.people{top:2452px;height:660px}
.people h2{color:var(--pink);margin-top:72px}
.person{position:absolute;top:139px;width:300px}
.person .photo{height:335px}
.person h4{font-family:"Poppins",sans-serif;font-weight:400;font-size:17px;color:var(--pink);margin-top:16px}
.person p{font-family:"Poppins",sans-serif;font-size:12px;color:#555;margin-top:4px}
.person .date{font-size:11px;color:#222;margin-top:6px}

.footer{top:3112px;height:202px;background:var(--footer)}
.contact{position:absolute;top:-32px;width:300px;text-align:center;font-family:"Poppins",sans-serif;font-size:12px;color:#aaa}
.contact .ic{width:64px;height:64px;border-radius:50%;background:var(--pink);margin:0 auto 14px;display:flex;align-items:center;justify-content:center}
.footer .rule{position:absolute;left:144px;width:912px;top:90px;border-top:1px solid #555}
.footer .links{position:absolute;left:144px;top:122px;font-size:11px;color:#aaa}
.footer .links span{margin:0 8px}
.footer .copy{position:absolute;left:144px;top:150px;font-size:11px;color:#aaa}
.footer .social{position:absolute;right:144px;top:130px;display:flex;gap:24px}
.footer .social i{width:14px;height:14px;border-radius:50%;background:#888;display:block}
</style>
</head>
<body>

<section class="topbar">
  <div class="brand"><span class="mark"></span>Funérailles Pâtes-Ferlande</div>
  <div class="phone">
    <svg width="14" height="14" viewBox="0 0 24 24"><path fill="#fff" d="M6.6 10.8a15 15 0 0 0 6.6 6.6l2.2-2.2c.3-.3.7-.4 1-.2 1.1.4 2.3.6 3.6.6.6 0 1 .4 1 1V20c0 .6-.4 1-1 1A17 17 0 0 1 3 4c0-.6.4-1 1-1h3.5c.6 0 1 .4 1 1 0 1.3.2 2.5.6 3.6.1.3 0 .7-.2 1z"/></svg>
    Such. : +32 (0) 61 / 48.20.73
  </div>
</section>

<nav class="nav" style="position:absolute;left:0;width:1200px;top:80px;height:40px;background:var(--pink)">
  <ul>
    <li class="active">HOME</li><li>OUR SOCIETY</li><li>WHAT TO DO IN CASE OF DEATH?</li><li>OUR SERVICES</li><li>THEY HAVE LEFT US</li><li>CONTACT</li>
  </ul>
</nav>

<section class="hero" role="img" aria-label="Black hearse parked in front of a stone church">
  <div class="arrow" style="left:0"><svg width="12" height="12" viewBox="0 0 12 12"><path d="M11 6H2M5 2 1 6l4 4" stroke="#fff" stroke-width="2" fill="none"/></svg></div>
  <div class="arrow" style="right:0"><svg width="12" height="12" viewBox="0 0 12 12"><path d="M1 6h9M7 2l4 4-4 4" stroke="#fff" stroke-width="2" fill="none"/></svg></div>
  <p class="caption">The tree owes the beauty of its fruits to the strength of its bark and the wisdom of its roots...</p>
</section>

<section class="about">
  <h2>Who We Are?</h2>
  <p>Founded in 1898 by Louis PÂTES, the family funeral home PÂTES &amp; FERLANDE's sole concern is to relieve the pain and sadness you endure when losing a loved one.<br>
  Whatever your origins, your beliefs or your traditions, we support you and offer a complete range of services and products adapted to your needs.<br>
  We organize the funeral and take care of the various administrative procedures related to the death.</p>
  <span class="btn">Read more</span>
</section>

<section class="services">
  <h2>Our Services</h2>
  <svg class="chev" style="left:54px;top:305px" width="18" height="26" viewBox="0 0 18 26"><path d="M14 3 4 13l10 10" stroke="#fff" stroke-width="3" fill="none"/></svg>
  <svg class="chev" style="right:54px;top:305px" width="18" height="26" viewBox="0 0 18 26"><path d="M4 3l10 10L4 23" stroke="#fff" stroke-width="3" fill="none"/></svg>
  <div class="cards">
    <div class="card">
      <div class="photo" role="img" aria-label="Wooden coffin with white lilies" style="background:linear-gradient(135deg,#c9a07a,#7a4a2a 60%,#222)"></div>
      <div class="icon"><svg width="34" height="40" viewBox="0 0 34 40"><path d="M6 36V14a11 11 0 0 1 22 0v22z" fill="none" stroke="#fff" stroke-width="2"/><path d="M17 12v14M12 17h10M3 37h28" stroke="#fff" stroke-width="2"/></svg></div>
      <h3>Complete funeral organization</h3>
      <p>Etiam vel massa elementum, bibendum tellus venenatis, feugiat massa. Curabitur venenatis lacinia ornare. Cras sollicitudin cursus dui placerat.</p>
      <span class="btn">Read more</span>
    </div>
    <div class="card">
      <div class="photo" role="img" aria-label="Bouquet of white lilies and roses" style="background:linear-gradient(135deg,#3d4a2a,#dfe3d4 55%,#5a6a3a)"></div>
      <div class="icon"><svg width="36" height="40" viewBox="0 0 36 40"><circle cx="18" cy="10" r="5" fill="none" stroke="#fff" stroke-width="2"/><circle cx="10" cy="16" r="4" fill="none" stroke="#fff" stroke-width="2"/><circle cx="26" cy="16" r="4" fill="none" stroke="#fff" stroke-width="2"/><path d="M10 22h16l-4 14h-8z" fill="none" stroke="#fff" stroke-width="2"/></svg></div>
      <h3>Order your flowers online</h3>
      <p>Etiam vel massa elementum, bibendum tellus venenatis, feugiat massa. Curabitur venenatis lacinia ornare. Cras sollicitudin cursus dui placerat.</p>
      <span class="btn">Read more</span>
    </div>
    <div class="card">
      <div class="photo" role="img" aria-label="Body under a white sheet in a preparation room" style="background:linear-gradient(135deg,#6a4a30,#e8e2d8 55%,#a7702e)"></div>
      <div class="icon"><svg width="40" height="40" viewBox="0 0 40 40"><path d="M10 4h8M12 4v12L5 32a3 3 0 0 0 3 4h12a3 3 0 0 0 3-4l-7-16V4M24 10h10M26 10v12a7 7 0 1 0 6 0V10" fill="none" stroke="#fff" stroke-width="2"/></svg></div>
      <h3>Embalming</h3>
      <p>Etiam vel massa elementum, bibendum tellus venenatis, feugiat massa. Curabitur venenatis lacinia ornare. Cras sollicitudin cursus dui placerat.</p>
      <span class="btn">Read more</span>
    </div>
  </div>
</section>

<section class="steps">
  <h2>What to do in case of death?</h2>
  <div class="acc open" style="top:129px">When the death occurs<svg width="14" height="8" viewBox="0 0 14 8"><path d="M0 8 7 0l7 8z" fill="#fff"/></svg></div>
  <div class="acc-body">The first steps to take in the event of death are generally difficult. That's why we invite you to read the few lines below to find useful information in case of death of a loved one.<br><span class="btn">Read more</span></div>
  <div class="acc closed" style="top:296px">Organize the funeral<svg width="14" height="8" viewBox="0 0 14 8"><path d="M0 0l7 8 7-8z" fill="#fff"/></svg></div>
  <div class="acc closed" style="top:352px">After the funeral<svg width="14" height="8" viewBox="0 0 14 8"><path d="M0 0l7 8 7-8z" fill="#fff"/></svg></div>
  <div class="acc closed" style="top:408px">To live your mourning<svg width="14" height="8" viewBox="0 0 14 8"><path d="M0 0l7 8 7-8z" fill="#fff"/></svg></div>
</section>

<section class="banner" role="img" aria-label="Pallbearers carrying a coffin topped with flowers">
  <p>Maecenas vel tortor accumsan quam<br>varius imperdiet vel eget elit</p>
  <span class="btn">Read more</span>
</section>

<section class="people">
  <h2>People Died Recently</h2>
  <svg class="chev" style="left:54px;top:300px" width="18" height="26" viewBox="0 0 18 26"><path d="M14 3 4 13l10 10" stroke="#777" stroke-width="3" fill="none"/></svg>
  <svg class="chev" style="right:54px;top:300px" width="18" height="26" viewBox="0 0 18 26"><path d="M4 3l10 10L4 23" stroke="#777" stroke-width="3" fill="none"/></svg>
  <div class="person" style="left:144px">
    <div class="photo" role="img" aria-label="Portrait of William" style="background:linear-gradient(160deg,#d9dcc8,#9a7c6a 55%,#5a4a58)"></div>
    <h4>William</h4><p>Nulla porttitor nibh ut mi feugiat</p><p class="date">6 June, 2019</p>
  </div>
  <div class="person" style="left:450px">
    <div class="photo" role="img" aria-label="Portrait of Madison" style="background:linear-gradient(160deg,#ddd,#a99a90 50%,#7a7a7a)"></div>
    <h4>Madison</h4><p>Aliquam dignissim elit nec mauris</p><p class="date">6 June, 2019</p>
  </div>
  <div class="person" style="left:756px">
    <div class="photo" role="img" aria-label="Portrait of Alexander" style="background:linear-gradient(160deg,#6a9a3a,#d9b48a 45%,#8a3a4a)"></div>
    <h4>Alexander</h4><p>Pellentesque vehicula nulla molestie</p><p class="date">6 June, 2019</p>
  </div>
</section>

<footer class="footer" style="position:absolute;left:0;width:1200px">
  <div class="contact" style="left:144px">
    <div class="ic"><svg width="22" height="28" viewBox="0 0 22 28"><path d="M11 0a11 11 0 0 0-11 11c0 8 11 17 11 17s11-9 11-17A11 11 0 0 0 11 0z" fill="#fff"/><circle cx="11" cy="11" r="4" fill="#d9268a"/></svg></div>
    rue des Tilleuls 42, 6800 VERVIN
  </div>
  <div class="contact" style="left:450px">
    <div class="ic"><svg width="26" height="26" viewBox="0 0 24 24"><path fill="#fff" d="M6.6 10.8a15 15 0 0 0 6.6 6.6l2.2-2.2c.3-.3.7-.4 1-.2 1.1.4 2.3.6 3.6.6.6 0 1 .4 1 1V20c0 .6-.4 1-1 1A17 17 0 0 1 3 4c0-.6.4-1 1-1h3.5c.6 0 1 .4 1 1 0 1.3.2 2.5.6 3.6.1.3 0 .7-.2 1z"/></svg></div>
    Such. : +32 (0) 61 / 48.20.73
  </div>
  <div class="contact" style="left:756px">
    <div class="ic"><svg width="26" height="20" viewBox="0 0 26 20"><rect width="26" height="20" rx="2" fill="#fff"/><path d="M1 2l12 9 12-9" stroke="#d9268a" stroke-width="2" fill="none"/></svg></div>
    contact@pfpf.be
  </div>
  <div class="rule"></div>
  <div class="links">Home<span>|</span>Our society<span>|</span>What to do in case of death?<span>|</span>Our services<span>|</span>They have left us<span>|</span>Contact</div>
  <div class="copy">Copyright © 2019 Pompes Funèbres Pâtes Ferlande.. All rights reserved.</div>
  <div class="social"><i></i><i></i></div>
</footer>

</body>
</html>
```